Bright Oak Consultant Services

I'm looking to create a flyer for my business to provide a consultant service. I will be providing the following below
Launch Your Business Today for only $150
(state fee not included)
Business Formation includes:
*Limited liability Corporation (LLC)
*Hale and Penwick Number
*FEIN
*Operation Agreement for partnership LLCs (For 2 or more member(s)
*Commercial Activity license (If needed for your Business )
*Same -day turnaround service with documents
Schedule your Appointment today
Call or text:413-902-6175
Email:MorvellCapitalCircle@quillpost.net
Target Market(s)
I want the flyer to attract people who wants to start a business but doesn’t know where to start. I want the flyer to stand out form the other consultant businesses.
Industry/Entity Type
Consultant
Requirements
Must have
- The State fee not included should be in small print
Highlight the price or service
Highlight the phrase "launch you business today"
Nice to have
- Different samples of colors, a variety
Should not have
- should not be all one color

```html
<!DOCTYPE html>
<html lang="en">
<head>
<meta charset="utf-8">
<title>Bright Oak Consultant Services – Business Formation Flyer</title>
<link href="https://fonts.googleapis.com/css2?family=Montserrat:wght@500;600;700;800;900&family=Oswald:wght@600;700&display=swap" rel="stylesheet">
<style>
  :root {
    --page-bg: #e4e4e4;
    --brand-red: #c00000;
    --brand-blue: #0066cc;
    --pill-blue: #1565d8;
    --ink: #1c1c1c;
    --white: #ffffff;
    --photo-light: #f2f2f2;
    --photo-mid: #c9ccd1;
    --photo-dark: #8e9096;
  }
  * { box-sizing: border-box; margin: 0; padding: 0; }
  html, body { width: 1200px; height: 1083px; overflow: hidden; }
  body {
    background: var(--page-bg);
    font-family: "Montserrat", Arial, sans-serif;
    position: relative;
  }
  .flyer {
    position: absolute;
    left: 210px;
    top: 36px;
    width: 780px;
    height: 1010px;
    background: var(--white);
    overflow: hidden;
    box-shadow: 0 10px 30px rgba(0,0,0,0.18);
  }
  .hero-photo {
    position: absolute;
    left: 0; top: 0;
    width: 780px; height: 480px;
    background: linear-gradient(160deg, var(--photo-dark) 0%, var(--photo-light) 45%, var(--photo-mid) 100%);
  }
  .flyer-shapes {
    position: absolute;
    left: 0; top: 0;
    width: 780px; height: 1010px;
  }
  .headline {
    position: absolute;
    left: 0; top: 484px;
    width: 780px;
    text-align: center;
    font-family: "Oswald", "Arial Narrow", sans-serif;
    font-weight: 700;
    font-size: 52px;
    line-height: 1.1;
    color: var(--white);
    letter-spacing: 0.5px;
    white-space: nowrap;
  }
  .price-box {
    position: absolute;
    left: 46px; top: 554px;
    width: 688px; height: 92px;
    background: var(--brand-red);
    display: flex;
    align-items: center;
    justify-content: center;
  }
  .price-text {
    font-weight: 900;
    font-size: 66px;
    color: var(--white);
    letter-spacing: 1px;
    white-space: nowrap;
  }
  .fee-note {
    position: absolute;
    right: 48px; top: 652px;
    font-size: 11px;
    font-weight: 500;
    color: var(--white);
  }
  .pill {
    position: absolute;
    background: var(--pill-blue);
    color: var(--white);
    border-radius: 24px;
    display: flex;
    align-items: center;
    justify-content: center;
    white-space: nowrap;
  }
  .section-pill {
    left: 172px; top: 682px;
    width: 436px; height: 44px;
    font-size: 22px;
    font-weight: 700;
  }
  .service-list {
    position: absolute;
    left: 0; top: 744px;
    width: 780px;
    list-style: none;
    color: var(--ink);
    font-size: 17px;
    font-weight: 500;
    line-height: 25px;
  }
  .service-list li {
    display: flex;
    align-items: center;
    justify-content: center;
    gap: 7px;
  }
  .tick { width: 15px; height: 15px; flex: none; }
  .cta-pill {
    left: 80px; top: 904px;
    width: 620px; height: 44px;
    font-size: 24px;
    font-weight: 700;
    letter-spacing: 0.5px;
    z-index: 2;
  }
  .contact-row {
    position: absolute;
    left: 0; bottom: 16px;
    width: 780px;
    display: flex;
    justify-content: center;
    gap: 46px;
    color: var(--white);
    font-weight: 700;
    font-size: 18px;
    font-style: normal;
  }
  .contact-item { display: flex; align-items: center; gap: 8px; }
  .contact-icon { width: 18px; height: 18px; }
</style>
</head>
<body>
  <main class="flyer">
    <div class="hero-photo" role="img" aria-label="Photo of a business person pressing a large launch button beside a blue toy rocket"></div>

    <svg class="flyer-shapes" viewBox="0 0 780 1010" aria-hidden="true">
      <polygon points="0,330 0,480 220,480" fill="var(--brand-red)"/>
      <polygon points="0,462 780,484 780,800 0,610" fill="var(--brand-blue)"/>
      <polygon points="0,610 520,738 0,740" fill="var(--brand-red)"/>
      <rect x="0" y="930" width="780" height="80" fill="var(--brand-red)"/>
    </svg>

    <h1 class="headline">LAUNCH YOUR BUSINESS TODAY</h1>
    <div class="price-box"><p class="price-text">FOR ONLY $150</p></div>
    <p class="fee-note">(state fee not included)</p>

    <h2 class="pill section-pill">Business Formation Includes:</h2>

    <ul class="service-list">
      <li><svg class="tick" viewBox="0 0 16 16"><circle cx="8" cy="8" r="6.8" fill="none" stroke="var(--brand-red)" stroke-width="1.4"/><path d="M5 8.2l2.1 2 4-4.2" fill="none" stroke="var(--brand-red)" stroke-width="1.4"/></svg>Limited liability Corporation (LLC)</li>
      <li><svg class="tick" viewBox="0 0 16 16"><circle cx="8" cy="8" r="6.8" fill="none" stroke="var(--brand-red)" stroke-width="1.4"/><path d="M5 8.2l2.1 2 4-4.2" fill="none" stroke="var(--brand-red)" stroke-width="1.4"/></svg>Hale and Penwick Number</li>
      <li><svg class="tick" viewBox="0 0 16 16"><circle cx="8" cy="8" r="6.8" fill="none" stroke="var(--brand-red)" stroke-width="1.4"/><path d="M5 8.2l2.1 2 4-4.2" fill="none" stroke="var(--brand-red)" stroke-width="1.4"/></svg>FEIN</li>
      <li><svg class="tick" viewBox="0 0 16 16"><circle cx="8" cy="8" r="6.8" fill="none" stroke="var(--brand-red)" stroke-width="1.4"/><path d="M5 8.2l2.1 2 4-4.2" fill="none" stroke="var(--brand-red)" stroke-width="1.4"/></svg>Operation Agreement for partnership LLCs (For 2 or more member(s)</li>
      <li><svg class="tick" viewBox="0 0 16 16"><circle cx="8" cy="8" r="6.8" fill="none" stroke="var(--brand-red)" stroke-width="1.4"/><path d="M5 8.2l2.1 2 4-4.2" fill="none" stroke="var(--brand-red)" stroke-width="1.4"/></svg>Commercial Activity license (If needed for your Business )</li>
      <li><svg class="tick" viewBox="0 0 16 16"><circle cx="8" cy="8" r="6.8" fill="none" stroke="var(--brand-red)" stroke-width="1.4"/><path d="M5 8.2l2.1 2 4-4.2" fill="none" stroke="var(--brand-red)" stroke-width="1.4"/></svg>Same -day turnaround service with documents</li>
    </ul>

    <p class="pill cta-pill">SCHEDULE YOUR APPOINTMENT TODAY</p>

    <address class="contact-row">
      <span class="contact-item">
        <svg class="contact-icon" viewBox="0 0 20 20"><circle cx="10" cy="10" r="8.5" fill="none" stroke="var(--white)" stroke-width="1.4"/><path d="M7.3 5.6c.5-.3 1-.2 1.2.3l.7 1.5c.2.4 0 .8-.3 1l-.6.4c.4 1 1.2 1.9 2.2 2.4l.5-.6c.3-.3.7-.4 1-.2l1.5.8c.4.2.5.7.2 1.1-.8 1.2-2 1.4-3.4.6-1.8-1-3.2-2.6-3.9-4.5-.4-1.2-.1-2.3.9-2.8z" fill="var(--white)"/></svg>
        413-902-6175
      </span>
      <span class="contact-item">
        <svg class="contact-icon" viewBox="0 0 20 20"><rect x="2" y="4.5" width="16" height="11" fill="none" stroke="var(--white)" stroke-width="1.4"/><path d="M2 4.5l8 6.5 8-6.5" fill="none" stroke="var(--white)" stroke-width="1.4"/></svg>
        MorvellCapitalCircle@quillpost.net
      </span>
    </address>
  </main>
</body>
</html>
```